Marlow Crest Homes Needs Business Card Design

Looking for a unique modern business card to fit my new Logo.
Name: Dean Marlow
Company: Marlow Crest Homes, LLC
Tag Line: Forever Framed Right
Email: marlowcresthomes@mailvista.test
Phone: (253) 555-0187
Website: www.marlowcresthomes.test
License: MARLOCH462QT

```html
<!DOCTYPE html>
<html lang="en">
<head>
<meta charset="utf-8">
<title>Marlow Crest Homes – Business Card</title>
<link rel="stylesheet" href="https://fonts.googleapis.com/css2?family=Montserrat:wght@300;400;600;700&display=swap">
<style>
  :root {
    --bg: #d3d3d3;
    --blue: #3597d0;
    --ink: #141414;
    --card-white: #ffffff;
    --card-black: #1c1c1c;
    --silver: #9a9a9a;
    --tag: #e8e8e8;
  }
  * { box-sizing: border-box; margin: 0; padding: 0; }
  html, body { width: 1200px; height: 913px; overflow: hidden; }
  body {
    background: var(--bg);
    font-family: "Montserrat", sans-serif;
    position: relative;
  }
  .card {
    position: absolute;
    top: 300px;
    width: 540px;
    height: 309px;
    border: 2px solid var(--blue);
  }
  .card--front { left: 30px; background: var(--card-white); }
  .card--back  { left: 630px; background: var(--card-black); }

  .brand {
    position: absolute;
    left: 32px;
    top: 30px;
    display: flex;
    align-items: center;
    gap: 10px;
    font-weight: 700;
    font-size: 17px;
    letter-spacing: 0.5px;
    color: var(--ink);
  }
  .brand__mark { width: 14px; height: 14px; background: var(--blue); }

  .contact { position: absolute; left: 32px; top: 92px; color: var(--ink); }
  .contact__name { color: var(--blue); font-weight: 700; font-size: 24px; letter-spacing: 1px; }
  .contact__role { font-weight: 400; font-size: 13px; margin-top: 2px; }
  .contact__company { font-weight: 700; font-size: 13px; margin-top: 3px; }
  .contact__list { list-style: none; margin-top: 8px; }
  .contact__item { display: flex; align-items: center; gap: 8px; font-size: 13px; line-height: 21px; }
  .contact__icon { width: 13px; height: 13px; fill: var(--blue); flex: none; }
  .contact__license { color: var(--blue); font-weight: 700; font-size: 14px; margin-top: 4px; letter-spacing: 0.3px; }

  .accent-bar {
    position: absolute;
    right: 0;
    top: 0;
    width: 18px;
    height: 100%;
    background: var(--blue);
  }

  .back__brand {
    position: absolute;
    left: 0; right: 0;
    top: 112px;
    text-align: center;
    font-weight: 700;
    font-size: 26px;
    letter-spacing: 1px;
    color: var(--silver);
  }
  .back__tagline {
    position: absolute;
    left: 0; right: 0;
    top: 222px;
    text-align: center;
    font-weight: 300;
    font-size: 14px;
    letter-spacing: 1px;
    color: var(--tag);
  }
</style>
</head>
<body>
  <section class="card card--front">
    <div class="brand"><span class="brand__mark"></span>MARLOW CREST HOMES</div>
    <div class="contact">
      <p class="contact__name">DEAN MARLOW</p>
      <p class="contact__role">Managing Director</p>
      <p class="contact__company">Marlow Crest Homes, LLC</p>
      <ul class="contact__list">
        <li class="contact__item">
          <svg class="contact__icon" viewBox="0 0 24 24"><path d="M6.6 10.8a15.1 15.1 0 0 0 6.6 6.6l2.2-2.2c.3-.3.7-.4 1-.2 1.1.4 2.3.6 3.6.6.6 0 1 .4 1 1V20c0 .6-.4 1-1 1A17 17 0 0 1 3 4c0-.6.4-1 1-1h3.5c.6 0 1 .4 1 1 0 1.3.2 2.5.6 3.6.1.3 0 .7-.2 1z"/></svg>
          (253) 555-0187
        </li>
        <li class="contact__item">
          <svg class="contact__icon" viewBox="0 0 24 24"><path d="M2 5h20v14H2z M2 5l10 8 10-8" /></svg>
          marlowcresthomes@mailvista.test
        </li>
        <li class="contact__item">
          <svg class="contact__icon" viewBox="0 0 24 24"><circle cx="12" cy="12" r="10"/></svg>
          www.marlowcresthomes.test
        </li>
      </ul>
      <p class="contact__license">License: MARLOCH462QT</p>
    </div>
    <div class="accent-bar"></div>
  </section>

  <section class="card card--back">
    <p class="back__brand">MARLOW CREST HOMES</p>
    <p class="back__tagline">FOREVER FRAMED RIGHT</p>
  </section>
</body>
</html>
```